Business Card - Professional Minimalist - Double sided

We appreciate minimalist logo/web/collateral designs that allow design to tell a story. We want to relay a professional image/approach but throwing in a splash of modern when we’re able so long as it’s not distracting. Think 75% classic corporate, 25% modern. Open to black or white design, not sure which might look the best.

Target Market(s)

Senior executives or related government affairs contacts within the agriculture, energy, and defense industries (i.e., potential clients) but located outside of Washington, DC. Most potential clients based in DC with be familiar with both of us and our shared history.

Industry/Entity Type

Consulting

Contact Information for Business Card

Name: Daniel R. Whitlock
Title: Co-Founder & Partner
Address: 418 Bramblewood Ave. SE | Suite 2716 | Washington, D.C. 20019
Phone: (202) 555-0187
Email: Daniel@HollerbyWhitlock.com

Font styles to use
Serif

Colors

Designer to choose only greyscale colors for use in the design.

Requirements
Must have
• Name: Daniel R. Whitlock
Phone: (202) 555-0187

```html
<!DOCTYPE html>
<html lang="en">
<head>
<meta charset="utf-8">
<title>Hollerby Whitlock Group — Business Card</title>
<link href="https://fonts.googleapis.com/css2?family=Marcellus&family=PT+Sans:wght@400;700&display=swap" rel="stylesheet">
<style>
  :root {
    --canvas: #e4e4e4;
    --card-dark: #231f20;
    --card-light: #f4f4f4;
    --ink: #4a4a4a;
    --ink-soft: #3c3c3c;
    --mark-on-dark: #8c8c8c;
    --mark-on-light: #555555;
    --accent-bar: #555555;
    --faint: #e6e6e6;
  }
  * { margin: 0; padding: 0; box-sizing: border-box; }
  html, body { width: 1200px; height: 960px; overflow: hidden; }
  body {
    background: var(--canvas);
    position: relative;
    font-family: "PT Sans", sans-serif;
    color: var(--ink);
  }
  .card {
    position: absolute;
    left: 309px;
    width: 584px;
    height: 333px;
    overflow: hidden;
  }
  .card--front { top: 122px; background: var(--card-dark); }
  .card--back  { top: 506px; background: var(--card-light); }

  .brand {
    position: absolute;
    display: flex;
    align-items: center;
    font-family: "Marcellus", serif;
    font-weight: 400;
    text-transform: uppercase;
    white-space: nowrap;
  }
  .brand__square { display: block; flex: none; }
  .card--front .brand {
    left: 98px; top: 138px;
    gap: 16px;
    font-size: 20px;
    letter-spacing: 1px;
    color: var(--mark-on-dark);
  }
  .card--front .brand__square { width: 56px; height: 56px; background: var(--mark-on-dark); }
  .card--back .brand {
    left: 41px; top: 41px;
    gap: 13px;
    font-size: 16px;
    letter-spacing: .6px;
    color: var(--mark-on-light);
  }
  .card--back .brand__square { width: 46px; height: 46px; background: var(--mark-on-light); }

  .backdrop-block {
    position: absolute;
    left: 0; top: 0;
    width: 218px; height: 216px;
    background: var(--faint);
    opacity: .55;
  }

  .holder {
    position: absolute;
    left: 41px; top: 252px;
  }
  .holder__name {
    font-size: 19px;
    font-weight: 700;
    letter-spacing: .3px;
    text-transform: uppercase;
    color: var(--ink);
    line-height: 1.2;
  }
  .holder__title {
    font-size: 15px;
    color: var(--ink-soft);
    margin-top: 2px;
  }
  .accent-bar {
    position: absolute;
    left: 0; top: 252px;
    width: 15px; height: 42px;
    background: var(--accent-bar);
  }

  .contact {
    position: absolute;
    left: 339px; top: 166px;
    font-size: 14.5px;
    line-height: 19.5px;
    color: var(--ink-soft);
  }
  .contact__address { margin-bottom: 12px; }
  .contact__row { display: flex; align-items: center; gap: 5px; }
  .contact__row svg { width: 13px; height: 13px; flex: none; fill: none; stroke: var(--ink-soft); stroke-width: 1.4; }
  .contact__row svg.solid { fill: var(--ink-soft); stroke: none; }
</style>
</head>
<body>
  <section class="card card--front" aria-label="Card front">
    <div class="brand">
      <span class="brand__square"></span>
      <span class="brand__name">Hollerby Whitlock Group</span>
    </div>
  </section>

  <section class="card card--back" aria-label="Card back">
    <div class="backdrop-block"></div>
    <div class="brand">
      <span class="brand__square"></span>
      <span class="brand__name">Hollerby Whitlock Group</span>
    </div>

    <div class="contact">
      <p class="contact__address">418 Bramblewood Ave. SE<br>Suite 2716<br>Washington, D.C. 20019</p>
      <p class="contact__row">
        <svg class="solid" viewBox="0 0 16 16" aria-hidden="true"><path d="M3.6 1.2l2.3 2.6-1.3 1.8c.9 2 2.4 3.5 4.4 4.4l1.8-1.3 2.6 2.3-1.5 2.2C7 14.6 1.4 9 1.3 2.7z"/></svg>
        (202) 555-0187
      </p>
      <p class="contact__row">
        <svg viewBox="0 0 16 16" aria-hidden="true"><rect x="1.5" y="3.5" width="13" height="9"/><path d="M1.5 3.5l6.5 5.5 6.5-5.5"/></svg>
        Daniel@HollerbyWhitlock.com
      </p>
      <p class="contact__row">
        <svg viewBox="0 0 16 16" aria-hidden="true"><circle cx="8" cy="8" r="6.2"/><ellipse cx="8" cy="8" rx="2.6" ry="6.2"/><path d="M1.8 8h12.4M3 4.6h10M3 11.4h10"/></svg>
        www.HollerbyWhitlock.com
      </p>
    </div>

    <div class="accent-bar"></div>
    <div class="holder">
      <p class="holder__name">Daniel R. Whitlock</p>
      <p class="holder__title">Co-Founder &amp; Partner</p>
    </div>
  </section>
</body>
</html>
```